Discreet simple classy for adult entertainment

I would like a matte black business card with gold writing for my business. Keeping it simple. Having my following:

Lina frost
Events. Entertainment. Promotions
0477250618

or alternatively could have what i had on my previous card below but i think i prefer the above as again - discretion.

Maybe a nice gold line thru the card or some other very simple design . Or not open to ideas/ can be doublesided if any good ideas with that.

included pics of my old bus card. not sure weather i want a photo on it or not. if i do it wont be the same pic. i kinda wanted a card that was discreet so if it was in someones wallet they wouldn't neccessarily realise it was from a stripper.

Target Market(s)

men

Industry/Entity Type

Business

Contact Information for Business Card

Lina frost
0477250618

Requirements
Nice to have
• i don't know i am really open to anything. im giving my cards to guys so something they can have in their wallet that is discreet preferably.

```html
<!DOCTYPE html>
<html lang="en">
<head>
<meta charset="utf-8">
<title>Lina Frost – Business Card</title>
<link rel="stylesheet" href="https://fonts.googleapis.com/css2?family=Archivo+Black&family=Roboto:wght@400;700&display=swap">
<style>
  :root {
    --card-matte: #141414;
    --gold: #c8a45a;
  }
  html, body {
    margin: 0;
    padding: 0;
    width: 1200px;
    height: 491px;
    overflow: hidden;
    background: var(--card-matte);
  }
  .business-card {
    display: block;
    width: 1200px;
    height: 491px;
  }
  .card-surface {
    fill: var(--card-matte);
  }
  .card-name {
    font-family: "Archivo Black", "Arial Black", sans-serif;
    font-size: 128px;
    fill: var(--gold);
  }
  .card-divider {
    stroke: var(--gold);
    stroke-width: 4;
  }
  .card-phone {
    font-family: "Roboto", Arial, sans-serif;
    font-weight: 700;
    font-size: 68px;
    fill: var(--gold);
  }
  .card-tagline {
    font-family: "Roboto", Arial, sans-serif;
    font-weight: 400;
    font-size: 60px;
    fill: var(--gold);
  }
</style>
</head>
<body>
  <svg class="business-card" viewBox="0 0 1200 491" xmlns="http://www.w3.org/2000/svg">
    <rect class="card-surface" x="0" y="0" width="1200" height="491"/>
    <text class="card-name" x="119" y="111" textLength="959" lengthAdjust="spacing">LINA FROST</text>
    <line class="card-divider" x1="170" y1="167" x2="1030" y2="167"/>
    <text class="card-phone" x="320" y="265" textLength="550" lengthAdjust="spacing">0477250618</text>
    <text class="card-tagline" x="3" y="481" textLength="1194" lengthAdjust="spacing">EVENTS | ENTERTAINMENT | PROMOTIONS</text>
  </svg>
</body>
</html>
```